Design some Business Cards for BrightLoop.

Attached please find the logo.

NO ART WORK OR PHOTOS OF THE PHONES ARE ALLOWED.

USE ONLY NATURAL (from logo) COLORS TO DESIGN THE BUSINESS CARD

Name : Oskar Penn
Phone : 312 748 2260
Toll Free : 1-888-615-2904
Fax : 1-888-615-WELK
Address : 7142 Marlow Pkwy NE, Atlanta, GA 30341

```html
<!DOCTYPE html>
<html lang="en">
<head>
<meta charset="utf-8">
<title>BrightLoop Business Cards</title>
<link href="https://fonts.googleapis.com/css2?family=Montserrat:wght@500;700;800&family=Open+Sans:wght@400;600&display=swap" rel="stylesheet">
<style>
  :root {
    --brand-blue: #2f7ab8;
    --brand-green: #5fb546;
    --paper: #ffffff;
    --stage: #e9eaec;
    --ink-light: #ffffff;
    --panel-width: 180px;
  }
  html, body {
    margin: 0;
    padding: 0;
    width: 1200px;
    height: 872px;
    overflow: hidden;
    background: var(--stage);
  }
  .canvas {
    position: relative;
    width: 1200px;
    height: 872px;
    display: flex;
    align-items: center;
    justify-content: center;
    gap: 40px;
  }
  .card {
    position: relative;
    width: 540px;
    height: 310px;
    overflow: hidden;
    box-shadow: 0 6px 18px rgba(0,0,0,0.12);
  }

  /* Front */
  .card--front {
    background: var(--brand-blue);
  }
  .card--front .accent-band {
    position: absolute;
    left: 0; right: 0; top: 0;
    height: 26px;
    background: var(--brand-green);
  }
  .front-brand {
    position: absolute;
    left: 0; right: 0; top: 26px; bottom: 0;
    display: flex;
    align-items: center;
    justify-content: center;
    gap: 14px;
  }
  .brand-dot {
    width: 34px;
    height: 34px;
    border-radius: 50%;
    background: var(--ink-light);
    flex: none;
  }
  .brand-name {
    font-family: 'Montserrat', sans-serif;
    font-weight: 800;
    font-size: 44px;
    letter-spacing: 0.5px;
    color: var(--ink-light);
    white-space: nowrap;
  }

  /* Back */
  .card--back {
    background: var(--brand-blue);
  }
  .back-logo-panel {
    position: absolute;
    top: 0; right: 0; bottom: 0;
    width: var(--panel-width);
    box-sizing: border-box;
    padding: 0 14px;
    background: var(--paper);
    display: flex;
    align-items: center;
    justify-content: center;
    gap: 8px;
  }
  .back-logo-panel .brand-dot {
    width: 14px;
    height: 14px;
    background: var(--brand-green);
  }
  .back-logo-panel .brand-name {
    font-size: 17px;
    letter-spacing: 0;
    color: var(--brand-blue);
  }
  .address-band {
    position: absolute;
    left: 0; bottom: 0;
    right: var(--panel-width);
    height: 30px;
    background: var(--brand-green);
    color: var(--ink-light);
    font-family: 'Open Sans', sans-serif;
    font-size: 12px;
    display: flex;
    align-items: center;
    padding-left: 22px;
  }
  .divider {
    position: absolute;
    left: 22px;
    right: calc(var(--panel-width) + 20px);
    top: 30px;
    height: 1px;
    background: var(--ink-light);
  }
  .contact-list {
    position: absolute;
    left: 22px;
    top: 48px;
    margin: 0;
    padding: 0;
    list-style: none;
    font-family: 'Open Sans', sans-serif;
    font-size: 13px;
    color: var(--ink-light);
  }
  .contact-list li {
    display: flex;
    align-items: center;
    gap: 10px;
    height: 22px;
  }
  .contact-icon {
    width: 14px;
    height: 14px;
    flex: none;
  }
  .holder {
    position: absolute;
    right: calc(var(--panel-width) + 20px);
    bottom: 48px;
    text-align: right;
    color: var(--ink-light);
  }
  .holder-name {
    font-family: 'Montserrat', sans-serif;
    font-weight: 700;
    font-size: 19px;
    letter-spacing: 1px;
    margin: 0;
  }
  .holder-title {
    font-family: 'Open Sans', sans-serif;
    font-size: 12px;
    margin: 2px 0 0;
  }
</style>
</head>
<body>
<main class="canvas">

  <section class="card card--front" aria-label="Business card front">
    <div class="accent-band"></div>
    <div class="front-brand">
      <span class="brand-dot"></span>
      <span class="brand-name">BrightLoop</span>
    </div>
  </section>

  <section class="card card--back" aria-label="Business card back">
    <div class="divider"></div>
    <ul class="contact-list">
      <li>
        <svg class="contact-icon" viewBox="0 0 14 14"><circle cx="7" cy="7" r="7" fill="#5fb546"/><path d="M4.6 3.6l1.3 0 .6 1.8-.9.6a5 5 0 0 0 2.4 2.4l.6-.9 1.8.6v1.3c0 .5-.4.8-.9.8A6 6 0 0 1 3.8 4.5c0-.5.3-.9.8-.9z" fill="#fff"/></svg>
        <span>312 748 2260</span>
      </li>
      <li>
        <svg class="contact-icon" viewBox="0 0 14 14"><circle cx="7" cy="7" r="7" fill="#5fb546"/><path d="M4.6 3.6l1.3 0 .6 1.8-.9.6a5 5 0 0 0 2.4 2.4l.6-.9 1.8.6v1.3c0 .5-.4.8-.9.8A6 6 0 0 1 3.8 4.5c0-.5.3-.9.8-.9z" fill="#fff"/></svg>
        <span>1-888-615-2904</span>
      </li>
      <li>
        <svg class="contact-icon" viewBox="0 0 14 14"><circle cx="7" cy="7" r="7" fill="#5fb546"/><rect x="4" y="6" width="6" height="4" fill="#fff"/><rect x="5" y="3.5" width="4" height="2.5" fill="#fff"/></svg>
        <span>1-888-615-WELK</span>
      </li>
      <li>
        <svg class="contact-icon" viewBox="0 0 14 14"><circle cx="7" cy="7" r="7" fill="#5fb546"/><rect x="3.5" y="4.5" width="7" height="5" fill="#fff"/><path d="M3.5 4.5L7 7.3l3.5-2.8" fill="none" stroke="#5fb546" stroke-width="0.8"/></svg>
        <span>Oskar@BrightLoopPhoneRepair.com</span>
      </li>
    </ul>
    <div class="holder">
      <p class="holder-name">OSKAR PENN</p>
      <p class="holder-title">Designation</p>
    </div>
    <div class="address-band">7142 Marlow Pkwy NE, Atlanta, GA 30341</div>
    <div class="back-logo-panel">
      <span class="brand-dot"></span>
      <span class="brand-name">BrightLoop</span>
    </div>
  </section>

</main>
</body>
</html>
```